Lorvenu online ordering platform looking for a great web design

Lorvenu - from the Vietnamese words Kiêm Lộc meaning financial success.
Background
Lorvenu is an online ordering platform for small retail businesses (corner stores). The idea is that small retailers will use the website to order their supplies. From this we will utilise the group buying to get better deals for them that they could not achieve individually.
We are looking for a simple but stylish design for our ordering page. The layout needs to be efficient, logical and self explanatory.
Products to be sold on the site are FMCG (fast moving consumer goods). Potential to be 000's of items.
Considerations
- end users are not technologically adept.
- Users are generally older so small print will not be well received.
- Use of touch screen monitors to select/change items so spacing in design is vital.
- Logical display of category and sub-categories.
- Easy selection of products to order as well as modification of quantity.
- Shopping cart with easy change of item quantity.
- List of items for ordering can be paginated.
- Items listed will have image for easy identification.
- Search box
- Format should be in psd (photoshop) or complete html/css
- All this information needs to be displayed on the one page.
Product information to contain the following:
- Image
- Price
- Product name
- Size
Area for prominent display of specials without crowding the product information.

```html
<!DOCTYPE html>
<html lang="en">
<head>
<meta charset="utf-8">
<title>Lorvenu – Sub Category</title>
<link href="https://fonts.googleapis.com/css2?family=Ubuntu:wght@400;500;700&family=Oswald:wght@500&display=swap" rel="stylesheet">
<style>
:root{
  --accent:#ef5128;
  --accent-dark:#d8401b;
  --ink:#4a4a4a;
  --muted:#9a9a9a;
  --line:#e2e2e2;
  --bar:#f3efe4;
  --bar-line:#d9d3c2;
  --topbar:#111;
  --footer:#efefef;
  --banner:#1db4c1;
}
*{box-sizing:border-box;margin:0;padding:0}
html,body{width:674px;height:1200px;overflow:hidden;background:#fff}
body{font-family:'Ubuntu',sans-serif;color:var(--ink);position:relative;font-size:8px}
a{color:inherit;text-decoration:none}

.topbar{position:absolute;left:0;top:0;width:674px;height:19px;background:var(--topbar)}
.topbar nav{position:absolute;right:72px;top:0;height:19px;display:flex;align-items:center;gap:14px;color:#fff;font-size:8px;font-weight:500}
.topbar .cart{display:flex;align-items:center;gap:4px;background:var(--accent);height:15px;padding:0 7px;border-radius:2px}
.topbar .cart svg{width:10px;height:10px}

.logo{position:absolute;left:72px;top:37px;font-size:17px;color:#8c8c8c;letter-spacing:.5px}

.mainnav{position:absolute;left:72px;top:76px;width:530px;height:19px;border:1px solid var(--line);background:#faf8f3;display:flex;align-items:center}
.mainnav a{font-size:8px;padding:0 13px;border-right:1px solid var(--line);line-height:11px}
.mainnav a.home{background:var(--accent);color:#fff;font-weight:700;height:19px;line-height:17px;width:56px;text-align:center;padding:0;margin:-1px 6px 0 -1px;border:1px solid var(--accent-dark)}
.mainnav .search{margin-left:auto;margin-right:3px;width:118px;height:14px;border:1px solid var(--line);background:#fff;font-size:7.5px;color:#999;padding:2px 5px;font-style:italic}

.banner{position:absolute;left:72px;top:98px;width:530px;height:109px;border:1px solid var(--line);padding:3px}
.banner .inner{position:relative;width:100%;height:100%;background:var(--banner);overflow:hidden}
.banner .photo{position:absolute;left:0;top:0;width:150px;height:100%;background:linear-gradient(90deg,#d9d9d6,#c4c6c5 60%,#1db4c1)}
.banner .offer{position:absolute;left:178px;top:14px;color:#fff;font-family:'Oswald',sans-serif;font-weight:500;display:flex;align-items:center}
.banner .offer .upto{writing-mode:vertical-rl;transform:rotate(180deg);font-size:17px;margin-right:3px}
.banner .offer .pct{font-size:62px;line-height:1}
.banner .learn{position:absolute;right:8px;bottom:6px;background:#fff;border:1px solid #ccc;font-size:8px;padding:3px 6px;color:#555}

.catbar{position:absolute;left:72px;width:530px;height:19px;background:var(--bar);border:1px solid var(--bar-line);display:flex;align-items:center;padding-left:3px}
.catbar a{font-size:8px;padding:0 5px;border-right:1px solid var(--bar-line);line-height:10px;color:#555}
.catbar a.active{background:var(--accent);color:#fff;font-weight:500;line-height:17px;border:1px solid var(--accent-dark);margin:0 2px}
.catbar.main{top:211px}
.catbar.sub{top:233px}

.crumb{position:absolute;left:73px;top:258px;font-size:6.5px;color:#555}
.crumb span{color:var(--accent)}
.page-title{position:absolute;left:73px;top:268px;font-size:15px;font-weight:500;color:var(--accent)}

.panel{position:absolute;left:72px;width:530px;border:1px solid var(--line)}
.panel h2{font-size:10.5px;font-weight:400;color:var(--accent);margin:6px 6px 0;padding-bottom:4px;border-bottom:1px solid var(--line)}
.panel h2 small{font-size:6.5px;color:#666}
.featured{top:292px;height:160px}
.latest{top:456px;height:578px}

.row{display:grid;grid-template-columns:repeat(5,1fr);margin:0 10px;padding:4px 0}
.latest .row{border-bottom:1px solid var(--line);height:134px}
.latest .row:nth-of-type(4){border-bottom:none}
.product{border-right:1px solid var(--line);padding:0 8px;height:125px}
.product:last-child{border-right:none}
.product .img{width:36px;height:72px;margin:2px auto 0;border-radius:8px 8px 6px 6px}
.img.green{background:linear-gradient(90deg,#2e9d22,#5fd43a 50%,#2e9d22)}
.img.blue{background:linear-gradient(90deg,#d8dde6,#fff 40%,#1f4fa8 85%);width:32px}
.img.white{background:linear-gradient(90deg,#cfd3d6,#fff 45%,#cfd3d6);width:34px}
.img.pink{background:linear-gradient(90deg,#b8103e,#ec3b6f 50%,#b8103e);width:28px}
.product .name{font-size:8px;line-height:10px;color:var(--accent);font-weight:500;margin-top:5px}
.product .meta{display:flex;justify-content:space-between;font-size:8px;line-height:10px;margin-top:2px}
.order{display:flex;justify-content:space-between;align-items:center;margin-top:4px;height:16px}
.qty{display:flex;border:1px solid #ccc;height:16px}
.qty span{width:16px;text-align:center;line-height:14px;font-size:9px}
.qty .step{background:#f3efe4;color:#555;font-weight:700}
.qty .count{width:18px;border-left:1px solid #ccc;border-right:1px solid #ccc;background:#fff}
.order .add{background:var(--accent);color:#fff;font-size:8px;font-weight:500;line-height:16px;padding:0 6px;border-radius:2px}

.pager{position:absolute;left:8px;bottom:4px;display:flex;gap:2px;font-size:7px;color:#bbb}
.pager span{border:1px solid #ddd;padding:1px 3px}
.pager span.on{border-color:var(--accent);color:var(--accent)}
.perpage{position:absolute;right:8px;bottom:4px;font-size:7px;color:#999}
.perpage span{border:1px solid #ddd;padding:1px 3px;margin-left:3px}

.footer{position:absolute;left:0;top:1050px;width:674px;height:150px;background:var(--footer)}
.fcol{position:absolute;top:18px;font-size:7px;line-height:11.6px;color:#a0a0a0}
.fcol h4{color:#444;font-weight:500;font-size:7px}
.newsletter{position:absolute;left:478px;top:18px;width:124px;font-size:7px;color:#444}
.newsletter .field{margin-top:4px;height:13px;border:1px solid #bbb;border-radius:7px;background:#fff;color:#999;padding:2px 6px;position:relative}
.newsletter .field i{position:absolute;right:1px;top:1px;width:9px;height:9px;border-radius:50%;background:#2a7fd4}
.social{display:flex;gap:4px;margin-top:6px}
.social span{width:16px;height:16px;background:#8a8f96;border-radius:2px}
.copy{position:absolute;left:74px;top:116px;font-size:7px;color:#a0a0a0}
.copy a{color:#333}
</style>
</head>
<body>

<header class="topbar"><nav><a href="#">Register</a><a href="#">Sign Up</a><a class="cart" href="#"><svg viewBox="0 0 10 10" fill="none" stroke="#fff" stroke-width="1"><path d="M0.5 1h1.5l1.2 5h5l1-3.5H2.6"/><circle cx="3.8" cy="8.3" r=".8"/><circle cx="7.6" cy="8.3" r=".8"/></svg>My Cart (2)</a></nav></header>
<div class="logo">LOGO HERE</div>

<nav class="mainnav">
  <a class="home" href="#">Home</a><a href="#">About</a><a href="#">Categories</a><a href="#">How it works</a><a href="#">Contact Us</a><a href="#">Support</a>
  <div class="search">search</div>
</nav>

<section class="banner">
  <div class="inner">
    <div class="photo" role="img" aria-label="Model in a white top holding a red bag strap"></div>
    <div class="offer"><span class="upto">UPTO</span><span class="pct">20% OFF</span></div>
    <a class="learn" href="#">Learn More</a>
  </div>
</section>

<nav class="catbar main"><a href="#">Lorem</a><a href="#">Ipsum</a><a href="#">Proin</a><a href="#">Gravida</a><a class="active" href="#">Main Category</a><a href="#">Nibhvel</a><a href="#">Auctor</a><a href="#">Aliquet</a><a href="#">Aenean</a></nav>
<nav class="catbar sub"><a href="#">Ipsum</a><a href="#">Nec sagittis</a><a href="#">Sem nibh id</a><a href="#">Duis sed</a><a href="#">Odio sit</a><a href="#">Amet nibh</a><a class="active" href="#">Sub Category</a><a href="#">Vulputate</a><a href="#">Cursus</a><a href="#">Amet</a></nav>

<div class="crumb">Home &gt; Main Category &gt; <span>Sub Category</span></div>
<h1 class="page-title">Sub Category</h1>

<section class="panel featured">
  <h2>Featured Products</h2>
  <div class="row">
    <div class="product"><div class="img green" role="img" aria-label="Green shampoo bottle"></div><div class="name">Product Name</div><div class="meta"><span>500ml</span><span>$2.59</span></div><div class="order"><div class="qty"><span class="step">−</span><span class="count">1</span><span class="step">+</span></div><a class="add" href="#">Add</a></div></div>
    <div class="product"><div class="img blue" role="img" aria-label="White and blue shampoo bottle"></div><div class="name">Product Name</div><div class="meta"><span>500ml</span><span>$2.59</span></div><div class="order"><div class="qty"><span class="step">−</span><span class="count">1</span><span class="step">+</span></div><a class="add" href="#">Add</a></div></div>
    <div class="product"><div class="img white" role="img" aria-label="White shampoo bottle"></div><div class="name">Product Name</div><div class="meta"><span>500ml</span><span>$2.59</span></div><div class="order"><div class="qty"><span class="step">−</span><span class="count">1</span><span class="step">+</span></div><a class="add" href="#">Add</a></div></div>
    <div class="product"><div class="img white" role="img" aria-label="White shampoo bottle"></div><div class="name">Product Name</div><div class="meta"><span>500ml</span><span>$2.59</span></div><div class="order"><div class="qty"><span class="step">−</span><span class="count">1</span><span class="step">+</span></div><a class="add" href="#">Add</a></div></div>
    <div class="product"><div class="img pink" role="img" aria-label="Pink shampoo bottle"></div><div class="name">Product Name</div><div class="meta"><span>500ml</span><span>$2.59</span></div><div class="order"><div class="qty"><span class="step">−</span><span class="count">1</span><span class="step">+</span></div><a class="add" href="#">Add</a></div></div>
  </div>
</section>

<section class="panel latest">
  <h2>Latest Arrivals <small>(see all)</small></h2>
  <div class="row">
    <div class="product"><div class="img green" role="img" aria-label="Green shampoo bottle"></div><div class="name">Product Name</div><div class="meta"><span>500ml</span><span>$2.59</span></div><div class="order"><div class="qty"><span class="step">−</span><span class="count">1</span><span class="step">+</span></div><a class="add" href="#">Add</a></div></div>
    <div class="product"><div class="img blue" role="img" aria-label="White and blue shampoo bottle"></div><div class="name">Product Name</div><div class="meta"><span>500ml</span><span>$2.59</span></div><div class="order"><div class="qty"><span class="step">−</span><span class="count">1</span><span class="step">+</span></div><a class="add" href="#">Add</a></div></div>
    <div class="product"><div class="img white" role="img" aria-label="White shampoo bottle"></div><div class="name">Product Name</div><div class="meta"><span>500ml</span><span>$2.59</span></div><div class="order"><div class="qty"><span class="step">−</span><span class="count">1</span><span class="step">+</span></div><a class="add" href="#">Add</a></div></div>
    <div class="product"><div class="img white" role="img" aria-label="White shampoo bottle"></div><div class="name">Product Name</div><div class="meta"><span>500ml</span><span>$2.59</span></div><div class="order"><div class="qty"><span class="step">−</span><span class="count">1</span><span class="step">+</span></div><a class="add" href="#">Add</a></div></div>
    <div class="product"><div class="img pink" role="img" aria-label="Pink shampoo bottle"></div><div class="name">Product Name</div><div class="meta"><span>500ml</span><span>$2.59</span></div><div class="order"><div class="qty"><span class="step">−</span><span class="count">1</span><span class="step">+</span></div><a class="add" href="#">Add</a></div></div>
  </div>
  <div class="row">
    <div class="product"><div class="img green" role="img" aria-label="Green shampoo bottle"></div><div class="name">Product Name</div><div class="meta"><span>500ml</span><span>$2.59</span></div><div class="order"><div class="qty"><span class="step">−</span><span class="count">1</span><span class="step">+</span></div><a class="add" href="#">Add</a></div></div>
    <div class="product"><div class="img blue" role="img" aria-label="White and blue shampoo bottle"></div><div class="name">Product Name</div><div class="meta"><span>500ml</span><span>$2.59</span></div><div class="order"><div class="qty"><span class="step">−</span><span class="count">1</span><span class="step">+</span></div><a class="add" href="#">Add</a></div></div>
    <div class="product"><div class="img white" role="img" aria-label="White shampoo bottle"></div><div class="name">Product Name</div><div class="meta"><span>500ml</span><span>$2.59</span></div><div class="order"><div class="qty"><span class="step">−</span><span class="count">1</span><span class="step">+</span></div><a class="add" href="#">Add</a></div></div>
    <div class="product"><div class="img white" role="img" aria-label="White shampoo bottle"></div><div class="name">Product Name</div><div class="meta"><span>500ml</span><span>$2.59</span></div><div class="order"><div class="qty"><span class="step">−</span><span class="count">1</span><span class="step">+</span></div><a class="add" href="#">Add</a></div></div>
    <div class="product"><div class="img pink" role="img" aria-label="Pink shampoo bottle"></div><div class="name">Product Name</div><div class="meta"><span>500ml</span><span>$2.59</span></div><div class="order"><div class="qty"><span class="step">−</span><span class="count">1</span><span class="step">+</span></div><a class="add" href="#">Add</a></div></div>
  </div>
  <div class="row">
    <div class="product"><div class="img green" role="img" aria-label="Green shampoo bottle"></div><div class="name">Product Name</div><div class="meta"><span>500ml</span><span>$2.59</span></div><div class="order"><div class="qty"><span class="step">−</span><span class="count">1</span><span class="step">+</span></div><a class="add" href="#">Add</a></div></div>
    <div class="product"><div class="img blue" role="img" aria-label="White and blue shampoo bottle"></div><div class="name">Product Name</div><div class="meta"><span>500ml</span><span>$2.59</span></div><div class="order"><div class="qty"><span class="step">−</span><span class="count">1</span><span class="step">+</span></div><a class="add" href="#">Add</a></div></div>
    <div class="product"><div class="img white" role="img" aria-label="White shampoo bottle"></div><div class="name">Product Name</div><div class="meta"><span>500ml</span><span>$2.59</span></div><div class="order"><div class="qty"><span class="step">−</span><span class="count">1</span><span class="step">+</span></div><a class="add" href="#">Add</a></div></div>
    <div class="product"><div class="img white" role="img" aria-label="White shampoo bottle"></div><div class="name">Product Name</div><div class="meta"><span>500ml</span><span>$2.59</span></div><div class="order"><div class="qty"><span class="step">−</span><span class="count">1</span><span class="step">+</span></div><a class="add" href="#">Add</a></div></div>
    <div class="product"><div class="img pink" role="img" aria-label="Pink shampoo bottle"></div><div class="name">Product Name</div><div class="meta"><span>500ml</span><span>$2.59</span></div><div class="order"><div class="qty"><span class="step">−</span><span class="count">1</span><span class="step">+</span></div><a class="add" href="#">Add</a></div></div>
  </div>
  <div class="row">
    <div class="product"><div class="img green" role="img" aria-label="Green shampoo bottle"></div><div class="name">Product Name</div><div class="meta"><span>500ml</span><span>$2.59</span></div><div class="order"><div class="qty"><span class="step">−</span><span class="count">1</span><span class="step">+</span></div><a class="add" href="#">Add</a></div></div>
    <div class="product"><div class="img blue" role="img" aria-label="White and blue shampoo bottle"></div><div class="name">Product Name</div><div class="meta"><span>500ml</span><span>$2.59</span></div><div class="order"><div class="qty"><span class="step">−</span><span class="count">1</span><span class="step">+</span></div><a class="add" href="#">Add</a></div></div>
    <div class="product"><div class="img white" role="img" aria-label="White shampoo bottle"></div><div class="name">Product Name</div><div class="meta"><span>500ml</span><span>$2.59</span></div><div class="order"><div class="qty"><span class="step">−</span><span class="count">1</span><span class="step">+</span></div><a class="add" href="#">Add</a></div></div>
    <div class="product"><div class="img white" role="img" aria-label="White shampoo bottle"></div><div class="name">Product Name</div><div class="meta"><span>500ml</span><span>$2.59</span></div><div class="order"><div class="qty"><span class="step">−</span><span class="count">1</span><span class="step">+</span></div><a class="add" href="#">Add</a></div></div>
    <div class="product"><div class="img pink" role="img" aria-label="Pink shampoo bottle"></div><div class="name">Product Name</div><div class="meta"><span>500ml</span><span>$2.59</span></div><div class="order"><div class="qty"><span class="step">−</span><span class="count">1</span><span class="step">+</span></div><a class="add" href="#">Add</a></div></div>
  </div>
  <div class="pager"><span>Previous</span><span class="on">1</span><span>2</span><span>3</span><span>4</span><span>5</span><span>&nbsp;&nbsp;Next&nbsp;&nbsp;</span></div>
  <div class="perpage">display per page<span>20 ▾</span></div>
</section>

<footer class="footer">
  <div class="fcol" style="left:74px"><h4>Why Us</h4>Features<br>Pricing<br>Site Gallery<br>Demo Video<br>Clients<br>Testimonials</div>
  <div class="fcol" style="left:141px"><h4>Company</h4>About Us<br>Press<br>Careers<br>Contact Us<br>Partner with Us</div>
  <div class="fcol" style="left:208px"><h4>Support</h4>Help<br>Contact Support<br>Video Tutorials<br>Privacy Policy<br>Terms of Service<br>Report Abuse</div>
  <div class="fcol" style="left:274px"><h4>Community</h4>Blog<br>Forums<br>Affiliates</div>
  <div class="fcol" style="left:343px"><h4>Contact Us</h4>14 Larkspur Lane<br>Gravida nibh vel velit auctor aliquet<br>Aenean sollicitudin<br>Dunmore<br><br>hello@lorvenu-mail.com<br>(555) 014 2271</div>
  <div class="newsletter">Subscribe Newsletter
    <div class="field">email address<i></i></div>
    <div style="margin-top:6px">Follow Us</div>
    <div class="social"><span></span><span></span><span></span><span></span></div>
  </div>
  <div class="copy">Copyright 2013. All rights reserved. <a href="#">Privacy Policy</a> | <a href="#">Terms of Service</a></div>
</footer>

</body>
</html>
```